Consulting Company Business Card

I am looking for a minimalist, classy, professional design on my business card. I would like it to be double-sided. I want to use the font and color scheme of my logo which are attached. Please be creative in the designs that you send me. I want to play off the design of my logo with the inner C that is Green and Blue broken up with the white.
Target Market(s)
Small Businesses
Industry/Entity Type
Consulting
Contact Information for Business Card
Dale M. Whitcombe, CPA CGMA, 555-014-2873, dwhitcombe@vorantaadvisory.example, www.vorantaadvisory.example

```html
<!DOCTYPE html>
<html lang="en">
<head>
<meta charset="utf-8">
<title>Voranta Advisory — Business Card</title>
<link rel="stylesheet" href="https://fonts.googleapis.com/css2?family=Montserrat:wght@300;400;600;700&display=swap">
<style>
  :root {
    --page: #ffffff;
    --navy-light: #213362;
    --navy-mid: #14235a;
    --navy-deep: #040936;
    --teal: #24a3a0;
    --white: #ffffff;
    --rule: rgba(255, 255, 255, 0.55);
    --shadow: rgba(0, 0, 0, 0.35);
  }
  * { box-sizing: border-box; margin: 0; padding: 0; }
  html, body {
    width: 734px;
    height: 1200px;
    overflow: hidden;
    background: var(--page);
    font-family: "Montserrat", Arial, sans-serif;
  }
  .sheet {
    position: relative;
    width: 734px;
    height: 1200px;
  }
  .card {
    position: absolute;
    left: 67px;
    width: 600px;
    height: 343px;
    background: linear-gradient(135deg, var(--navy-light) 0%, var(--navy-mid) 50%, var(--navy-deep) 100%);
    box-shadow: 0 4px 10px var(--shadow);
    color: var(--white);
    overflow: hidden;
  }
  .card--front { top: 217px; }
  .card--back { top: 640px; }

  /* Brand lockup */
  .brand {
    position: absolute;
    display: flex;
    flex-direction: column;
    align-items: center;
    color: var(--white);
    font-weight: 700;
  }
  .brand__dot {
    border-radius: 50%;
    background: var(--teal);
  }
  .brand__name {
    line-height: 1;
    text-align: center;
  }
  .brand__name span { display: block; }
  .brand__sub { letter-spacing: 0.32em; margin-left: 0.32em; }

  .card--front .brand {
    left: 0; right: 0; top: 74px;
  }
  .card--front .brand__dot { width: 62px; height: 62px; margin-bottom: 18px; }
  .card--front .brand__name { font-size: 38px; }
  .card--front .brand__sub { font-size: 14px; margin-top: 6px; }

  .front__web {
    position: absolute;
    left: 0; right: 0; top: 268px;
    text-align: center;
    font-size: 15px;
    font-weight: 300;
    letter-spacing: 0.06em;
  }

  .card--back .brand {
    left: 392px; width: 148px; top: 40px;
  }
  .card--back .brand__dot { width: 46px; height: 46px; margin-bottom: 12px; }
  .card--back .brand__name { font-size: 26px; }
  .card--back .brand__sub { font-size: 10px; margin-top: 4px; }

  .person {
    position: absolute;
    left: 40px; top: 146px;
  }
  .person__name {
    color: var(--teal);
    font-size: 23px;
    font-weight: 700;
    letter-spacing: 0.04em;
    text-transform: uppercase;
  }
  .person__title {
    font-size: 15px;
    font-weight: 700;
    margin-top: 4px;
    letter-spacing: 0.02em;
  }
  .person__rule {
    position: absolute;
    left: 146px; top: 192px;
    width: 393px; height: 1px;
    background: var(--rule);
  }
  .contact {
    position: absolute;
    left: 40px; top: 218px;
    list-style: none;
  }
  .contact__item {
    display: flex;
    align-items: center;
    gap: 9px;
    font-size: 14.5px;
    font-weight: 600;
    height: 25px;
    letter-spacing: 0.01em;
  }
  .contact__icon { width: 13px; height: 13px; flex: none; }
</style>
</head>
<body>
<main class="sheet">

  <section class="card card--front" aria-label="Card front">
    <div class="brand">
      <div class="brand__dot"></div>
      <div class="brand__name">
        <span class="brand__main">VORANTA</span>
        <span class="brand__sub">ADVISORY</span>
      </div>
    </div>
    <p class="front__web">www.vorantaadvisory.example</p>
  </section>

  <section class="card card--back" aria-label="Card back">
    <div class="brand">
      <div class="brand__dot"></div>
      <div class="brand__name">
        <span class="brand__main">VORANTA</span>
        <span class="brand__sub">ADVISORY</span>
      </div>
    </div>

    <div class="person">
      <p class="person__name">Dale M. Whitcombe</p>
      <p class="person__title">CPA CGMA</p>
    </div>
    <div class="person__rule"></div>

    <ul class="contact">
      <li class="contact__item">
        <svg class="contact__icon" viewBox="0 0 24 24" aria-hidden="true">
          <path fill="#24a3a0" d="M6.6 10.8a15.1 15.1 0 0 0 6.6 6.6l2.2-2.2a1 1 0 0 1 1-.25 11.4 11.4 0 0 0 3.6.57 1 1 0 0 1 1 1V20a1 1 0 0 1-1 1A17 17 0 0 1 3 4a1 1 0 0 1 1-1h3.5a1 1 0 0 1 1 1c0 1.25.2 2.45.57 3.57a1 1 0 0 1-.25 1z"/>
        </svg>
        <span>555-014-2873</span>
      </li>
      <li class="contact__item">
        <svg class="contact__icon" viewBox="0 0 24 24" aria-hidden="true">
          <rect x="2" y="5" width="20" height="14" fill="#24a3a0"/>
          <path d="M2 5l10 8 10-8" fill="none" stroke="#14235a" stroke-width="1.8"/>
        </svg>
        <span>dwhitcombe@vorantaadvisory.example</span>
      </li>
      <li class="contact__item">
        <svg class="contact__icon" viewBox="0 0 24 24" aria-hidden="true">
          <g fill="none" stroke="#24a3a0" stroke-width="2">
            <circle cx="12" cy="12" r="9.5"/>
            <ellipse cx="12" cy="12" rx="4.5" ry="9.5"/>
            <path d="M2.5 12h19M4 7h16M4 17h16"/>
          </g>
        </svg>
        <span>www.vorantaadvisory.example</span>
      </li>
    </ul>
  </section>

</main>
</body>
</html>
```